Business Card for boutique psychology business

Business card for boutique psychology practice in Melbourne. I want them to be relatively simply with the logo and backing colour taking up the front side. Then, text on the back, with my name; professional title (Clinical Psychologist); website - torvinpsychology.com.au; email: hello@torvinpsychology.com.au; insta: @torvin.psychology.emdr
Back should also have the words: Connect. Integrate. Evolve
Fonts used for logo are: Mikea Demo and Gotham Medium. Use something for back text that will compliment these.
Brand colours uploaded below. I'd like to see options in both olive and blush.

```html
<!DOCTYPE html>
<html lang="en">
<head>
<meta charset="utf-8">
<title>Torvin Psychology — Business Card</title>
<link rel="stylesheet" href="https://fonts.googleapis.com/css2?family=Montserrat:wght@400;500;700&display=swap">
<style>
  :root {
    --blush: #ebcebd;
    --olive: #3e3c25;
    --olive-light: #8a8470;
    --ink-soft: #ffffff;
    --stage: #d4d4d4;
    --stage-dark: #a9a9a9;
  }
  * { box-sizing: border-box; margin: 0; padding: 0; }
  html, body { width: 1200px; height: 788px; overflow: hidden; }
  body {
    background: linear-gradient(180deg, var(--stage) 0%, var(--stage-dark) 100%);
    font-family: "Montserrat", sans-serif;
    position: relative;
  }
  .card {
    position: absolute;
    top: 239px;
    width: 540px;
    height: 310px;
    background: var(--blush);
    border-radius: 22px;
    overflow: hidden;
    box-shadow: 0 14px 30px rgba(0,0,0,.22);
  }
  .card--back { left: 45px; }
  .card--front { left: 615px; }

  .wordmark {
    color: var(--olive);
    font-weight: 500;
    text-align: center;
    letter-spacing: .01em;
    line-height: 1;
  }
  .card--back .wordmark { position: absolute; top: 34px; left: 0; right: 0; font-size: 30px; }
  .card--front .wordmark {
    position: absolute; top: 50%; left: 0; right: 0;
    transform: translateY(-50%); font-size: 52px;
  }

  .identity {
    position: absolute; top: 130px; right: 300px; text-align: right;
  }
  .identity__name { color: var(--olive); font-weight: 700; font-size: 15px; letter-spacing: .03em; }
  .identity__title { color: var(--ink-soft); font-weight: 400; font-size: 13px; margin-top: 4px; }

  .divider {
    position: absolute; top: 112px; left: 270px; width: 1px; height: 92px;
    background: var(--olive-light);
  }

  .contacts { position: absolute; top: 112px; left: 286px; list-style: none; }
  .contacts li {
    display: flex; align-items: center; gap: 8px;
    color: var(--ink-soft); font-size: 12px; line-height: 23px;
  }
  .contacts svg { width: 12px; height: 12px; flex: none; fill: var(--olive); }

  .tagline-band {
    position: absolute; left: 0; right: 0; bottom: 22px; height: 22px;
    background: linear-gradient(90deg, var(--olive) 0%, var(--olive) 35%, var(--olive-light) 55%, var(--olive) 80%);
    color: var(--ink-soft);
    font-size: 11px; letter-spacing: .04em;
    display: flex; align-items: center; justify-content: center; gap: 8px;
  }
</style>
</head>
<body>
  <section class="card card--back" aria-label="Card back">
    <p class="wordmark">Torvin Psychology</p>

    <div class="identity">
      <p class="identity__name">MARA LINDQVIST</p>
      <p class="identity__title">Clinical Psychologist</p>
    </div>

    <div class="divider"></div>

    <ul class="contacts">
      <li>
        <svg viewBox="0 0 12 12" aria-hidden="true"><path d="M2.5 1 4.5 1 5.3 3.6 4 4.6c.6 1.4 1.9 2.7 3.4 3.4l1-1.3 2.6.8V9.5C11 10.3 10.3 11 9.5 11 5 11 1 7 1 2.5 1 1.7 1.7 1 2.5 1Z"/></svg>
        (987) 555-0142
      </li>
      <li>
        <svg viewBox="0 0 12 12" aria-hidden="true"><path d="M1 2.5h10v7H1Z M1 2.5 6 6.5 11 2.5" fill="none" stroke="#3e3c25" stroke-width="1.2"/></svg>
        hello@torvinpsychology.com.au
      </li>
      <li>
        <svg viewBox="0 0 12 12" aria-hidden="true"><g fill="none" stroke="#3e3c25" stroke-width="1.1"><circle cx="6" cy="6" r="5"/><ellipse cx="6" cy="6" rx="2.2" ry="5"/><path d="M1 6h10"/></g></svg>
        www.torvinpsychology.com.au
      </li>
      <li>
        <svg viewBox="0 0 12 12" aria-hidden="true"><circle cx="6" cy="6" r="5"/></svg>
        @torvin.psychology.emdr
      </li>
    </ul>

    <div class="tagline-band">
      <span>Connect</span><span>•</span><span>Integrate</span><span>•</span><span>Evolve</span>
    </div>
  </section>

  <section class="card card--front" aria-label="Card front">
    <p class="wordmark">Torvin Psychology</p>
  </section>
</body>
</html>
```